Powerpoint Template for Consulting Group
Creative Brief
We want a Powerpoint template that can be used to bid on consulting projects, to sell our services. I am looking for a design that's modern and showcases our technical experience in web development and marketing, while being visually creative. Our website is: www.tealwhiskgroup.example. I'm open to any color palettes, but want a clean, modern look and feel to the powerpoint.
Corporate
This project requires a title slide template and a template for the remaining slides in the presentation. The template should be built as a PowerPoint template file and be compatible with Microsoft Office 2013. The template slide layouts should include (at least): sample title and text block; sample title and bulleted text (with multiple bullet levels); sample title and content; and sample title and graph (e.g. bar chart, with default colors matching the overall template design). I am only looking for the creatives/designs. We will fill the content on our own.

```html
<!DOCTYPE html>
<html lang="en">
<head>
<meta charset="utf-8">
<title>tealwhisk — presentation template</title>
<link href="https://fonts.googleapis.com/css2?family=Montserrat:wght@500;700&family=Raleway:wght@300;400&family=Open+Sans:wght@400;600&display=swap" rel="stylesheet">
<style>
:root{
  --page:#e9e6e1;
  --ink:#111111;
  --black:#0b0b0b;
  --white:#ffffff;
  --muted:#8a8a8a;
  --body:#333333;
  --lorem:#d9d9d9;
  --splash-a:#f4c9d8;
  --splash-b:#c9def2;
  --splash-c:#f6e7b8;
  --photo-a:#0d2a44;
  --photo-b:#1f6f93;
  --photo-c:#061522;
  --bar-1:#111111;
  --bar-2:#d4d4d4;
  --bar-3:#8c8c8c;
  --bar-4:#555555;
}
*{box-sizing:border-box;margin:0;padding:0}
html,body{width:1200px;height:1000px;overflow:hidden;background:var(--page)}
body{position:relative;font-family:"Open Sans",Arial,sans-serif;color:var(--body)}
.slide{position:absolute;width:540px;height:390px;background:var(--white);overflow:hidden;box-shadow:0 6px 18px rgba(0,0,0,.18)}
.slide--title{left:40px;top:305px}
.slide--services{left:620px;top:70px}
.slide--graph{left:620px;top:540px}
.splash{position:absolute;left:0;top:0;width:100%;height:95px;
  background:radial-gradient(ellipse at 20% 60%,var(--splash-a),transparent 55%),
             radial-gradient(ellipse at 60% 40%,var(--splash-b),transparent 55%),
             radial-gradient(ellipse at 90% 70%,var(--splash-c),transparent 50%),var(--white)}
.band{position:absolute;left:0;width:100%;background:var(--black);color:var(--white)}
.footer{position:absolute;left:0;bottom:0;width:100%;height:24px;background:var(--black);
  font-size:8px;letter-spacing:2px;color:var(--muted);display:flex;align-items:center;justify-content:center}
.wordmark{font-family:"Montserrat",Arial,sans-serif;font-weight:500;letter-spacing:-.5px}
.tagline{font-family:"Montserrat",Arial,sans-serif;font-weight:500;font-size:7px;letter-spacing:1.4px}
.notch{position:absolute}
/* title slide */
.slide--title .band{top:95px;height:58px}
.slide--title .brand{position:absolute;left:40px;top:6px;color:var(--white)}
.slide--title .wordmark{font-size:34px;line-height:34px}
.slide--title .tagline{font-size:9px;display:block;margin-top:3px}
.photo{position:absolute;left:0;top:153px;width:100%;height:213px;
  background:radial-gradient(ellipse at 35% 55%,var(--photo-b),transparent 60%),linear-gradient(160deg,var(--photo-a),var(--photo-c))}
.subtitle{position:absolute;left:205px;top:162px;font-size:8px;color:var(--white)}
/* content slides */
.slide .head-band{top:80px;height:46px}
.slide-title{position:absolute;left:22px;top:86px;font-family:"Raleway",Arial,sans-serif;font-weight:300;font-size:28px;color:var(--white)}
.corner-brand{position:absolute;right:22px;top:42px;text-align:left}
.corner-brand .wordmark{font-size:26px;color:var(--ink);line-height:28px;display:block}
.corner-brand .tagline{color:var(--white);display:block;margin-top:14px}
.columns{position:absolute;left:22px;right:22px;top:150px;display:grid;grid-template-columns:1fr 1fr;gap:22px}
.service h3{font-size:7px;font-weight:600;color:var(--ink);margin-bottom:3px}
.service p{font-size:6.5px;line-height:9px;margin-bottom:10px}
/* graph slide */
.slide--graph .dark-body{position:absolute;left:0;top:126px;width:100%;height:240px;background:var(--black)}
.lorem{position:absolute;left:22px;top:142px;width:215px;font-size:7px;line-height:10px;color:var(--lorem)}
.chart{position:absolute;left:262px;top:138px;width:258px;height:212px;background:var(--white)}
</style>
</head>
<body>

<section class="slide slide--title">
  <div class="splash" role="img" aria-label="Soft watercolor splash in pink, blue and yellow"></div>
  <div class="band">
    <div class="brand"><span class="wordmark">tealwhisk</span><span class="tagline">MARKETING AND DESIGN GROUP</span></div>
  </div>
  <div class="photo" role="img" aria-label="Photo of a hand touching glowing business chart icons on a dark blue screen"></div>
  <svg class="notch" style="left:60px;top:152px" width="40" height="14" viewBox="0 0 40 14"><polygon points="0,0 40,0 20,14" fill="#0b0b0b"/></svg>
  <p class="subtitle">Expert Design, Development and Marketing for Successful Results</p>
  <div class="footer">www.tealwhiskgroup.example</div>
</section>

<section class="slide slide--services">
  <div class="splash" role="img" aria-label="Soft watercolor splash in pink, blue and yellow"></div>
  <div class="band head-band"></div>
  <h2 class="slide-title">Services</h2>
  <svg class="notch" style="left:40px;top:125px" width="34" height="12" viewBox="0 0 34 12"><polygon points="0,0 34,0 17,12" fill="#0b0b0b"/></svg>
  <div class="corner-brand"><span class="wordmark">tealwhisk</span><span class="tagline">MARKETING AND DESIGN GROUP</span></div>
  <div class="columns">
    <div>
      <div class="service"><h3>Creative and Experience Design</h3><p>Our team shapes clear, memorable brands and interfaces. We pair visual craft with user research to build work that connects and converts across every channel.</p></div>
      <div class="service"><h3>Website Strategy, Implementation and Management</h3><p>It's not enough to design a good-looking website. Our developers build fast, accessible sites with search optimisation in mind so your customers find you first.</p></div>
    </div>
    <div>
      <div class="service"><h3>Market Research</h3><p>A results-driven market research team uses both primary and third-party data to craft insights for improving consistent engagement.</p></div>
      <div class="service"><h3>Content Strategy and Management</h3><p>Brovamark's content team has proven success in content strategy, including SEO, social media, editorial planning and creation, link building, copywriting and analysis.</p></div>
      <div class="service"><h3>Digital Advertising</h3><p>We provide the most profitable strategies for search, paid social, display and remarketing.</p></div>
    </div>
  </div>
  <div class="footer">www.tealwhiskgroup.example</div>
</section>

<section class="slide slide--graph">
  <div class="splash" role="img" aria-label="Soft watercolor splash in pink, blue and yellow"></div>
  <div class="band head-band"></div>
  <h2 class="slide-title">Graph</h2>
  <div class="dark-body"></div>
  <svg class="notch" style="left:40px;top:125px" width="34" height="12" viewBox="0 0 34 12"><polygon points="0,0 34,0 17,12" fill="#0b0b0b"/></svg>
  <div class="corner-brand"><span class="wordmark">tealwhisk</span><span class="tagline">MARKETING AND DESIGN GROUP</span></div>
  <p class="lorem">Lorem Ipsum is simply dummy text of the printing and typesetting industry. Lorem Ipsum has been the industry's standard dummy text ever since the 1500s, when an unknown printer took a galley of type and scrambled it to make a type specimen book. It has survived not only five centuries, but also the leap into electronic typesetting, remaining essentially unchanged. It was popularised in the 1960s with the release of Sheetrune sheets containing Lorem Ipsum passages, and more recently with desktop publishing software like Quillpage Composer including versions of Lorem Ipsum.</p>
  <svg class="chart" viewBox="0 0 258 212" role="img" aria-label="Bar chart with four bars">
    <g font-family="Open Sans, Arial, sans-serif" font-size="7" fill="#666" text-anchor="end">
      <text x="26" y="195">0.0</text><text x="26" y="160">1.0</text><text x="26" y="125">2.0</text>
      <text x="26" y="90">3.0</text><text x="26" y="55">4.0</text><text x="26" y="20">5.0</text>
    </g>
    <g stroke="#e2e2e2" stroke-width="0.7">
      <line x1="32" y1="193" x2="246" y2="193"/><line x1="32" y1="158" x2="246" y2="158"/>
      <line x1="32" y1="123" x2="246" y2="123"/><line x1="32" y1="88" x2="246" y2="88"/>
      <line x1="32" y1="53" x2="246" y2="53"/><line x1="32" y1="18" x2="246" y2="18"/>
    </g>
    <rect x="44" y="123" width="38" height="70" fill="var(--bar-1)"/>
    <rect x="97" y="106" width="38" height="87" fill="var(--bar-2)" stroke="#aaa" stroke-width="0.7"/>
    <rect x="150" y="22" width="38" height="171" fill="var(--bar-3)"/>
    <rect x="203" y="96" width="38" height="97" fill="var(--bar-4)"/>
  </svg>
  <div class="footer">www.tealwhiskgroup.example</div>
</section>

</body>
</html>
```